Business Card & Logo Design Project

I am looking for a slick/simple design for a logo and business card, for a music Producer/Mixer/Engineer.

I'm based in Tokyo, Japan and I help my clients polish up their creation to major radio/TV status. My clients pay me for my taste, sense of balance expertise and creative direction/

Design should give impression of seal of quality, professionalism, and enthusiasm need some sort of a logo like design for "vantrix productions".

Please don't include music notes or instruments or anything musically related and anything samurai or ninja or too much Japan in them on the design.

I like clever, slick stuff that's not too obvious.
I also like a smooth gradation type transition. My favorite color is deep dark blue/

Good Luck and Thank you for your effort.
Updates

I would like a two-sided design for this one.
One side with "vantrix productions" (all lower case) on, and the other side with my name and contact info.

Please also consider portrait position (or direction).  (as opposed to landscape) 

Target Market(s)

My primary targets are artists & bands, who want absolute best for their creation.

Industry/Entity Type

Business

Requirements
Must have
• Two-Sided
1, vantrix productions
2, Kenji Harumoto, Producer/Mixer/Engineer, +81 090 4827 3516, brambleway@mailnest.example
Nice to have
• Any suggestions are welcome//
Should not have
• Anything music related images.
(e.g. CD, music notations, instruments etc.)

```html
<!DOCTYPE html>
<html lang="en">
<head>
<meta charset="utf-8">
<title>vantrix productions – business card</title>
<link rel="stylesheet" href="https://fonts.googleapis.com/css2?family=Quicksand:wght@500;600&family=Arimo:wght@400&display=swap">
<style>
  :root {
    --backdrop: #cbcbcb;
    --navy-deep: #261f5f;
    --navy-glow: #0a4f93;
    --paper: #ffffff;
    --ink: #262163;
  }
  * { box-sizing: border-box; margin: 0; padding: 0; }
  html, body {
    width: 1200px; height: 844px; overflow: hidden;
    background: var(--backdrop);
  }
  .sheet {
    position: relative; width: 1200px; height: 844px;
    display: flex; justify-content: center; align-items: center; gap: 90px;
  }
  .card {
    position: relative; width: 400px; height: 560px;
    box-shadow: 2px 3px 6px rgba(0,0,0,0.25);
    overflow: hidden;
  }

  /* Front */
  .card--front {
    background: radial-gradient(circle at 55% 48%, var(--navy-glow) 0%, var(--navy-deep) 62%);
    color: var(--paper);
  }
  .brand-mark {
    position: absolute; left: 0; right: 0; top: 180px;
    display: flex; align-items: center; justify-content: center; gap: 16px;
    font-family: "Quicksand", sans-serif; font-weight: 600;
  }
  .brand-mark__dot {
    width: 34px; height: 34px; border-radius: 50%; background: currentColor;
  }
  .brand-mark__name { font-size: 58px; line-height: 1; letter-spacing: 1px; }
  .card--front .wordmark {
    position: absolute; left: 0; right: 0; bottom: 92px;
    text-align: center;
    font-family: "Quicksand", sans-serif; font-weight: 600;
    font-size: 33px; line-height: 1; white-space: nowrap;
  }

  /* Back */
  .card--back { background: var(--paper); color: var(--ink); }
  .card--back .brand-mark { top: 120px; color: var(--ink); }
  .card--back .brand-mark__name { font-size: 50px; }
  .card--back .brand-mark__dot { width: 28px; height: 28px; }

  .band {
    position: absolute; left: 50px; width: 300px; height: 18px;
    background: linear-gradient(90deg, var(--navy-deep) 0%, var(--navy-glow) 50%, var(--navy-deep) 100%);
    clip-path: polygon(4% 0, 100% 0, 96% 100%, 0 100%);
  }
  .band--upper { top: 356px; }
  .band--lower { top: 452px; }

  .contact {
    position: absolute; left: 0; right: 0; text-align: center;
    font-family: "Arimo", Arial, sans-serif; line-height: 1.15;
    white-space: nowrap;
  }
  .contact__name { top: 388px; font-size: 28px; }
  .contact__role { top: 426px; font-size: 16px; }
  .contact__phone { top: 484px; font-size: 16px; }
  .contact__email { top: 508px; font-size: 16px; }
</style>
</head>
<body>
  <main class="sheet">
    <section class="card card--front" aria-label="Card front">
      <div class="brand-mark">
        <span class="brand-mark__dot" aria-hidden="true"></span>
        <span class="brand-mark__name">vantrix</span>
      </div>
      <p class="wordmark">vantrix productions</p>
    </section>

    <section class="card card--back" aria-label="Card back">
      <div class="brand-mark">
        <span class="brand-mark__dot" aria-hidden="true"></span>
        <span class="brand-mark__name">vantrix</span>
      </div>
      <div class="band band--upper" aria-hidden="true"></div>
      <p class="contact contact__name">Kenji Harumoto</p>
      <p class="contact contact__role">Producer/Mixer/Engineer</p>
      <div class="band band--lower" aria-hidden="true"></div>
      <p class="contact contact__phone">+81 090 4827 3516</p>
      <p class="contact contact__email">brambleway@mailnest.example</p>
    </section>
  </main>
</body>
</html>
```